Soap Company Looking To Design New Soap Scent Boxes

we are looking to create a soap box similar to pa grunwell. we would like the circle cut out on the top right corner of the box. we are looking for a design that will allow us to use different color base banners for different soap scents (like pa. grunwell). we want the soap name scents to be large and readable on the bottom banner (like pa.grunwell). we have included our brand figure (logo) and some previous older soap box designs that we were making before the brand figure. the box dims are attached.

```html
<!DOCTYPE html>
<html lang="en">
<head>
<meta charset="utf-8">
<title>Hour of Thyme – Plumeria Soap Box Dieline</title>
<link rel="stylesheet" href="https://fonts.googleapis.com/css2?family=Montserrat:wght@500;700;800;900&family=Patrick+Hand&display=swap">
<style>
  :root {
    --kraft: #dcc9ab;
    --kraft-fibre: #cdb894;
    --wine: #7b151b;
    --wine-deep: #6a1016;
    --cut-line: #e2303a;
    --fold-mark: #3fa0d8;
    --white: #ffffff;
    --sage-green: #4f8a55;
    --art-tone-a: #e7b94d;
    --art-tone-b: #3f8a3c;
    --sketch-tone: #c8ac8a;
  }
  html, body {
    margin: 0;
    padding: 0;
    width: 1200px;
    height: 894px;
    overflow: hidden;
    background: var(--kraft);
  }
  .dieline {
    display: block;
    width: 1200px;
    height: 894px;
  }
  .kraft-base { fill: var(--kraft); }
  .kraft-fibres line { stroke: var(--kraft-fibre); stroke-width: 0.6; opacity: 0.55; }
  .scent-banner { fill: var(--wine); }
  .cut-line { fill: none; stroke: var(--cut-line); stroke-width: 0.8; }
  .fold-mark { fill: none; stroke: var(--fold-mark); stroke-width: 0.8; }
  .brand-name { font-family: "Montserrat", sans-serif; font-weight: 900; fill: var(--wine-deep); }
  .tag-band { fill: var(--wine); }
  .tag-text { font-family: "Montserrat", sans-serif; font-weight: 700; fill: var(--white); letter-spacing: 0.6px; }
  .ingredients { font-family: "Patrick Hand", sans-serif; fill: var(--wine); letter-spacing: 0.3px; }
  .ingredients .lead { font-size: 9.5px; }
  .ingredients .tagline { font-size: 9.5px; }
  .art-placeholder-sketch { fill: var(--sketch-tone); opacity: 0.55; }
  .icon-line { fill: none; stroke: var(--white); stroke-width: 1.1; stroke-linecap: round; stroke-linejoin: round; }
  .feature-label { font-family: "Montserrat", sans-serif; font-weight: 700; font-size: 5px; fill: var(--white); letter-spacing: 0.3px; text-anchor: middle; }
  .scent-list-title { font-family: "Montserrat", sans-serif; font-weight: 700; font-size: 4.6px; fill: var(--white); letter-spacing: 0.5px; }
  .scent-list { font-family: "Montserrat", sans-serif; font-weight: 500; font-size: 5.2px; fill: var(--wine); text-anchor: middle; }
  .scent-side-label { font-family: "Montserrat", sans-serif; font-weight: 700; font-size: 6px; fill: var(--white); text-anchor: middle; letter-spacing: 0.4px; }
  .window-cutout { fill: var(--wine); }
  .product-type { font-family: "Montserrat", sans-serif; font-weight: 500; font-size: 13px; fill: var(--white); text-anchor: middle; }
  .scent-name { font-family: "Montserrat", sans-serif; font-weight: 900; font-size: 29px; fill: var(--white); text-anchor: middle; letter-spacing: 0.5px; }
  .net-weight { font-family: "Montserrat", sans-serif; font-weight: 800; font-size: 7px; fill: var(--white); }
  .net-weight-badge { fill: var(--white); }
  .net-weight-badge-text { font-family: "Montserrat", sans-serif; font-weight: 800; font-size: 7px; fill: var(--wine); }
  .lotus-line { fill: none; stroke: var(--sage-green); stroke-width: 1.1; stroke-linejoin: round; }
  .motto { font-family: "Montserrat", sans-serif; font-weight: 700; font-size: 5.6px; fill: var(--sage-green); text-anchor: middle; letter-spacing: 0.6px; }
</style>
</head>
<body>
<svg class="dieline" viewBox="0 0 808 600" preserveAspectRatio="none" xmlns="http://www.w3.org/2000/svg">
  <defs>
    <linearGradient id="portraitTones" x1="0" y1="0" x2="1" y2="1">
      <stop offset="0" stop-color="var(--art-tone-b)"/>
      <stop offset="0.55" stop-color="var(--art-tone-a)"/>
      <stop offset="1" stop-color="#f4e2c8"/>
    </linearGradient>
  </defs>

  <rect class="kraft-base" x="0" y="0" width="808" height="600"/>
  <g class="kraft-fibres">
    <line x1="40" y1="0" x2="40" y2="600"/><line x1="95" y1="0" x2="95" y2="600"/>
    <line x1="150" y1="0" x2="150" y2="600"/><line x1="210" y1="0" x2="210" y2="600"/>
    <line x1="270" y1="0" x2="270" y2="600"/><line x1="360" y1="0" x2="360" y2="600"/>
    <line x1="470" y1="0" x2="470" y2="600"/><line x1="540" y1="0" x2="540" y2="600"/>
    <line x1="620" y1="0" x2="620" y2="600"/><line x1="740" y1="0" x2="740" y2="600"/>
  </g>

  <!-- Scent colour banner -->
  <path class="scent-banner" d="M15 295 L70 295 C150 295 220 332 330 332 L423 334 C500 336 600 336 662 330 C705 324 740 302 795 300 L795 437 L15 437 Z"/>

  <!-- Dieline -->
  <g class="cut-line">
    <path d="M58 172 L58 40 Q58 30 68 30 L320 30 Q330 30 330 40 L330 172"/>
    <path d="M330 172 L330 102 L405 102 L412 135 L423 172"/>
    <path d="M693 172 L700 135 L708 102 L795 102 L795 437"/>
    <path d="M58 172 L15 185 L15 425 L58 437"/>
    <path d="M58 172 L795 172"/>
    <path d="M58 437 L795 437"/>
    <path d="M58 172 L58 437 M330 172 L330 437 M423 172 L423 437 M693 172 L693 437"/>
    <path d="M330 437 L340 470 L415 470 L423 437"/>
    <path d="M693 437 L703 470 L785 470 L795 437"/>
    <path d="M423 437 L423 570 Q423 580 433 580 L683 580 Q693 580 693 570 L693 437"/>
    <path d="M58 75 L330 75"/>
    <path d="M423 525 L693 525"/>
  </g>
  <g class="fold-mark">
    <path d="M72 73 Q76 73 76 77"/>
    <path d="M316 73 Q312 73 312 77"/>
    <path d="M437 523 Q433 523 433 527"/>
    <path d="M679 523 Q683 523 683 527"/>
  </g>

  <!-- Back panel -->
  <g class="back-panel">
    <text class="brand-name" x="70" y="210" font-size="19">Hour of Thyme</text>
    <rect class="tag-band" x="136" y="214" width="98" height="10"/>
    <text class="tag-text" x="185" y="221.5" font-size="6" text-anchor="middle">ARTISAN SOAP BAR</text>
    <text class="ingredients">
      <tspan class="lead" x="80" y="241"><tspan font-size="12">OUR</tspan> BATH SOAPS COLLECTION ARE INFUSED</tspan>
      <tspan x="70" y="251" font-size="7.6">WITH ALL-ORGANIC INGREDIENTS INCLUDING</tspan>
      <tspan x="70" y="259" font-size="7.6">COCONUT OIL, CANOLA OIL, SOYBEAN OIL,</tspan>
      <tspan x="70" y="267" font-size="7.6">SHEA BUTTER, WATER, SODIUM HYDROXIDE (LYE),</tspan>
      <tspan x="70" y="275" font-size="7.6">OLIVE POMACE OIL, SUNFLOWER OIL, FRAGRANCE</tspan>
      <tspan class="tagline" x="100" y="291">THIS IS NATURE IN A BAR!</tspan>
    </text>
    <rect class="art-placeholder-sketch" x="256" y="230" width="70" height="96" rx="32"
          role="img" aria-label="Line sketch of the brand figure with a sprig of sage"/>

    <g class="icon-line">
      <path d="M119 346 L119 332 M123 344 L123 328 M127 344 L127 329 M131 346 L131 333 M119 346 Q117 352 122 356 L130 356 Q134 352 133 344 L135 340"/>
      <path d="M184 352 L192 352 L200 348 L208 350 M184 344 L192 342 L200 344 M198 338 Q194 330 200 324 Q206 330 202 338 Z M200 338 L200 330"/>
      <rect x="249" y="340" width="16" height="11" rx="3"/>
      <circle cx="266" cy="334" r="4"/><circle cx="272" cy="329" r="2.5"/><circle cx="259" cy="333" r="2"/>
    </g>
    <text class="feature-label" x="126" y="389">HANDMADE</text>
    <text class="feature-label" x="196" y="389">ALL-NATURAL</text>
    <text class="feature-label" x="196" y="396">INGREDIENTS</text>
    <text class="feature-label" x="264" y="389">VARIETY OF</text>
    <text class="feature-label" x="264" y="396">SOAP SCENTS</text>
  </g>

  <!-- Side panel: scents -->
  <g class="side-panel">
    <rect class="tag-band" x="345" y="185" width="60" height="8"/>
    <text class="scent-list-title" x="375" y="191" text-anchor="middle">AVAILABLE SCENTS</text>
    <text class="scent-list">
      <tspan x="376" y="203">Cedarwood Tea Tree</tspan>
      <tspan x="376" y="210">Charcoal Aloe</tspan>
      <tspan x="376" y="217">Cool Water</tspan>
      <tspan x="376" y="224">Dead Sea Scrub</tspan>
      <tspan x="376" y="231">Eucalyptus Aloe</tspan>
      <tspan x="376" y="238">Hydrangea</tspan>
      <tspan x="376" y="245">Jasmine Lime Scrub</tspan>
      <tspan x="376" y="252">Mango Papaya</tspan>
      <tspan x="376" y="259">Mountain Air</tspan>
      <tspan x="376" y="266">Nag Champa</tspan>
      <tspan x="376" y="273">Plumeria</tspan>
      <tspan x="376" y="280">Pomegranate Cherry</tspan>
      <tspan x="376" y="287">Raspberry Bush</tspan>
      <tspan x="376" y="294">Raspberry Vanilla</tspan>
      <tspan x="376" y="301">Sandalwood Rose</tspan>
      <tspan x="376" y="308">Tangerine Grapefruit</tspan>
      <tspan x="376" y="315">Wild Passion</tspan>
      <tspan x="376" y="322">Wildflowers</tspan>
    </text>
    <text class="scent-side-label" x="376" y="368">PLUMERIA</text>
    <g class="icon-line" transform="translate(376 386)">
      <path d="M0 -2 Q-4 -12 0 -13 Q4 -12 0 -2 Z"/>
      <path d="M0 -2 Q-4 -12 0 -13 Q4 -12 0 -2 Z" transform="rotate(72)"/>
      <path d="M0 -2 Q-4 -12 0 -13 Q4 -12 0 -2 Z" transform="rotate(144)"/>
      <path d="M0 -2 Q-4 -12 0 -13 Q4 -12 0 -2 Z" transform="rotate(216)"/>
      <path d="M0 -2 Q-4 -12 0 -13 Q4 -12 0 -2 Z" transform="rotate(288)"/>
    </g>
  </g>

  <!-- Front panel -->
  <g class="front-panel">
    <circle class="window-cutout" cx="606" cy="221" r="34"/>
    <ellipse cx="516" cy="240" rx="52" ry="53" fill="url(#portraitTones)"
             role="img" aria-label="Brand figure portrait in a green hood inside an oval frame"/>
    <text class="brand-name" x="558" y="315" font-size="22" text-anchor="middle">Hour of Thyme</text>
    <text class="product-type" x="558" y="351">NATURAL SOAP</text>
    <text class="scent-name" x="558" y="400">PLUMERIA</text>
    <text class="net-weight" x="463" y="422">COLD PRESSED</text>
    <rect class="net-weight-badge" x="526" y="415" width="64" height="9.5" rx="1"/>
    <text class="net-weight-badge-text" x="529" y="422.5">ARTISAN SOAP</text>
    <text class="net-weight" x="593" y="422">Net Wt. 5oz / 140g</text>
  </g>

  <!-- Right side panel -->
  <g class="right-panel">
    <g class="lotus-line">
      <path d="M741 226 Q733 214 741 200 Q749 214 741 226 Z"/>
      <path d="M740 226 Q726 222 723 208 Q735 210 740 226 Z"/>
      <path d="M742 226 Q756 222 759 208 Q747 210 742 226 Z"/>
      <path d="M724 226 L758 226"/>
    </g>
    <text class="motto"><tspan x="742" y="244">REJUVENATE</tspan><tspan x="742" y="252">YOUR MIND</tspan><tspan x="742" y="260">BODY AND</tspan><tspan x="742" y="268">SOUL</tspan></text>
    <g class="icon-line">
      <path d="M716 410 L720 404 L724 410 M726 414 L722 420 L716 420 M714 416 L712 410 L718 408"/>
      <path d="M734 420 L746 420 M736 410 Q740 404 744 410 M740 410 L740 420 M734 416 L736 412 M746 416 L744 412"/>
      <path d="M756 410 L764 410 M757 410 L758 421 L762 421 L763 410 M752 414 L754 408 M750 422 L752 416"/>
    </g>
  </g>
</svg>
</body>
</html>
```